Talvok Engineering Business card Design

We need to make business cards for our NDT and inspection company. The company is called Talvok Engineering. We want a professional modern feel business card. We have just completed the remaking of our website and would like to have business cards with the same feel and colours. The final design should communicate professionalism and cutting edge tech.

Target Market(s)

We sell to B2B Business clients. Our customer is an engineer or decision maker in the mechanical engineering / Oil and gas field.

Contact Information for Business Card

Please see the current business cards that we have uploaded to get the details. You can also look at our Website www.talvok-eng.example for more.

Requirements
Must have
• Less is more
Nice to have
• Less is more

```html
<!DOCTYPE html>
<html lang="en">
<head>
<meta charset="utf-8">
<title>Talvok Engineering Business Card</title>
<link href="https://fonts.googleapis.com/css2?family=Roboto:wght@300;400;500;700&display=swap" rel="stylesheet">
<style>
  :root {
    --backdrop: #3a2a22;
    --card: #242424;
    --edge: #a4191d;
    --accent: #b01f24;
    --text: #f2f2f2;
    --muted: #8a8a8a;
    --rule: #9a9a9a;
  }
  * { box-sizing: border-box; margin: 0; padding: 0; }
  html, body { width: 1200px; height: 716px; overflow: hidden; }
  body {
    background: var(--backdrop);
    font-family: "Roboto", sans-serif;
    color: var(--text);
    position: relative;
  }
  .card {
    position: absolute;
    top: 200px;
    width: 540px;
    height: 316px;
    background: var(--card);
    border: 3px solid var(--edge);
    border-radius: 3px;
    box-shadow: 0 14px 30px rgba(0,0,0,.45);
    display: flex;
    align-items: center;
  }
  .card--back { left: 40px; }
  .card--front { left: 620px; }
  .brand {
    width: 230px;
    display: flex;
    flex-direction: column;
    align-items: center;
    gap: 14px;
  }
  .brand__mark {
    width: 120px; height: 120px;
    border-radius: 50%;
    border: 2px solid var(--muted);
  }
  .card--front .brand__mark { border-color: var(--accent); }
  .brand__name {
    font-weight: 500;
    font-size: 17px;
    letter-spacing: .3px;
    color: var(--text);
  }
  .divider {
    width: 1px;
    height: 200px;
    background: var(--rule);
  }
  .services {
    list-style: none;
    padding-left: 26px;
    font-size: 12.5px;
    line-height: 17px;
  }
  .services li { position: relative; padding-left: 12px; }
  .services li::before {
    content: ""; position: absolute; left: 0; top: 6px;
    width: 5px; height: 5px; border-radius: 50%; background: var(--accent);
  }
  .card--back .web {
    position: absolute; left: 0; bottom: 28px; width: 230px;
    text-align: center; font-size: 12.5px;
  }
  .contact { padding-left: 26px; }
  .contact__name { color: var(--accent); font-weight: 700; font-size: 24px; }
  .contact__role { font-weight: 300; font-size: 19px; margin-bottom: 10px; }
  .contact__address { font-weight: 300; font-size: 16px; line-height: 20px; margin-bottom: 10px; }
  .contact__line {
    display: flex; align-items: center; gap: 10px;
    font-weight: 300; font-size: 16px; line-height: 24px;
  }
  .contact__line svg { width: 14px; height: 14px; flex: none; }
  .hl { color: var(--accent); }
</style>
</head>
<body>
  <section class="card card--back">
    <div class="brand">
      <div class="brand__mark"></div>
      <div class="brand__name">Talvok Engineering</div>
    </div>
    <div class="divider"></div>
    <ul class="services">
      <li>API 653 Tank Inspections</li>
      <li>API 570 Pipeline Inspections</li>
      <li>API 510 Pressure Vessel Inspections</li>
      <li>Welding Inspection</li>
      <li>Electrical Inspection</li>
      <li>OCTG Inspections</li>
      <li>Lifting Equipment Inspections</li>
      <li>Non-Destructive Testing</li>
      <li>UT / PT / MT / RT / VT</li>
      <li>Advanced NDT</li>
      <li>PAUT / MFL / ILI</li>
      <li>Engineering Projects</li>
    </ul>
    <div class="web">www.talvok-eng.example</div>
  </section>

  <section class="card card--front">
    <div class="brand">
      <div class="brand__mark"></div>
      <div class="brand__name">Talvok Engineering</div>
    </div>
    <div class="divider"></div>
    <div class="contact">
      <div class="contact__name">Elias Marend</div>
      <div class="contact__role">Manager</div>
      <div class="contact__address">P.O. BOX 55012-80200<br>Port Lemari</div>
      <div class="contact__line">
        <svg viewBox="0 0 24 24" fill="#b01f24"><path d="M6.6 10.8a15 15 0 0 0 6.6 6.6l2.2-2.2c.3-.3.7-.4 1-.2 1.1.4 2.3.6 3.6.6.6 0 1 .4 1 1V20c0 .6-.4 1-1 1A17 17 0 0 1 3 4c0-.6.4-1 1-1h3.5c.6 0 1 .4 1 1 0 1.3.2 2.5.6 3.6.1.3 0 .7-.2 1z"/></svg>
        + 254 20 555 0142/3
      </div>
      <div class="contact__line">
        <svg viewBox="0 0 24 24" fill="none" stroke="#b01f24" stroke-width="2"><rect x="3" y="5" width="18" height="14" rx="1"/><path d="M3 6l9 7 9-7"/></svg>
        info@talvok-eng.example
      </div>
      <div class="contact__line">
        <svg viewBox="0 0 24 24" fill="none" stroke="#b01f24" stroke-width="2"><circle cx="12" cy="12" r="9"/><path d="M3 12h18M12 3c3 3 3 15 0 18M12 3c-3 3-3 15 0 18"/></svg>
        <span>www.<span class="hl">talvok-eng</span>.example</span>
      </div>
    </div>
  </section>
</body>
</html>
```